business card for a shoe shop

we would like a business card for a family owned shoe shop.
With this information included.
Dunleavy's Shoe Store
Family owned since 1947

then on other side
Dunleavy's Shoe Store
Footwear fitting specialist
Phone: 9471 2386
218 Tarn St, Wexley Heights 3091
(cnr. Corrigan Rd and Tarn St)
dunleavyshoes218@quillmail.example
if could incorporate the purple color on card i have attached.

```html
<!DOCTYPE html>
<html lang="en">
<head>
<meta charset="utf-8">
<title>Dunleavy's Shoe Store – Business Card</title>
<link rel="stylesheet" href="https://fonts.googleapis.com/css2?family=Old+Standard+TT:wght@700&family=Open+Sans:wght@500&family=Lato:wght@400&display=swap">
<style>
  :root {
    --brand-purple: #652b8f;
    --card-white: #ffffff;
    --ink: #1c1c1c;
    --backdrop: #d3d4d6;
  }
  * { margin: 0; padding: 0; box-sizing: border-box; }
  html, body {
    width: 900px; height: 1200px; overflow: hidden;
    background: var(--backdrop);
  }
  .canvas { position: relative; width: 900px; height: 1200px; }
  .card {
    position: absolute;
    width: 656px; height: 375px;
    border-radius: 11px;
    overflow: hidden;
  }
  .card--front { left: 122px; top: 190px; background: var(--brand-purple); }
  .card--back { left: 124px; top: 622px; background: var(--card-white); }
  .line {
    position: absolute; left: 0; right: 0;
    text-align: center; transform: translateY(-50%);
    white-space: nowrap;
  }
  .store-name {
    font-family: "Old Standard TT", "Century Schoolbook", serif;
    font-weight: 700;
  }
  .card--front .store-name { top: 183px; font-size: 48px; color: var(--card-white); letter-spacing: 0.5px; }
  .tagline {
    top: 322px;
    font-family: "Open Sans", sans-serif; font-weight: 500;
    font-size: 18px; letter-spacing: 1px; color: var(--card-white);
  }
  .card--back .store-name { top: 98px; font-size: 35px; color: var(--brand-purple); }
  .contact {
    font-family: "Lato", sans-serif; font-weight: 400;
    color: var(--ink); letter-spacing: 1.1px;
  }
  .specialty { top: 141px; font-size: 17px; }
  .phone { top: 207px; font-size: 19.5px; letter-spacing: 1.4px; }
  .address { font-size: 17px; }
  .address--street { top: 242px; }
  .address--corner { top: 268px; }
  .email { top: 304px; font-size: 17px; }
  .social { top: 337px; font-size: 17px; display: flex; justify-content: center; align-items: center; gap: 9px; }
  .social-dot { width: 20px; height: 20px; border-radius: 50%; background: var(--brand-purple); display: inline-block; }
  .accent-band {
    position: absolute; left: 0; right: 0; bottom: 0;
    height: 14px; background: var(--brand-purple);
  }
</style>
</head>
<body>
<main class="canvas">
  <section class="card card--front" aria-label="Card front">
    <h1 class="line store-name">Dunleavy's Shoe Store</h1>
    <p class="line tagline">Family owned since 1947</p>
  </section>

  <section class="card card--back" aria-label="Card back">
    <h2 class="line store-name">Dunleavy's Shoe Store</h2>
    <p class="line contact specialty">Footwear fitting specialist</p>
    <p class="line contact phone">Phone: 9471 2386</p>
    <p class="line contact address address--street">218 Tarn St, Wexley Heights 3091</p>
    <p class="line contact address address--corner">(cnr. Corrigan Rd and Tarn St)</p>
    <p class="line contact email">dunleavyshoes218@quillmail.example</p>
    <p class="line contact social"><span class="social-dot" aria-hidden="true"></span><span>/dunleavyshoes</span></p>
    <div class="accent-band"></div>
  </section>
</main>
</body>
</html>
```